Web page update/ Create new non flash site

I have a flash web page, created by my ex girlfriend through some kind of web design service. I want to take all of the information that I have on the page and put it together in a similar manner on a non-flash page.I want to add a lot of pictures, update the logo to the one i had made on pixel forge and reword a few things to reflect the the direction my business has gone in, in the past couple years since I made the site.. I also can't figure out why when people e-mail me from my page, I get the e-mail but no message, happens all the time and makes me think I'm losing business. My main problem is that I don't know what service was used in the past to create this page or what information someone would need to be able to work on it more. I also have another domain name that I want connected to it. the existing web page is at www.ferrowbuilders.example

Target Market(s)

I originally made this web page thinking that i was going to be in the remodeling business, but the majority of the work i get is for high end commercial and residential millwork and carpentry installations. I mainly will be advertising to other general contractors, but I want to keep the same feel that it has now, how it is mainly talking to homeowners that are thinking about hiring me to do some sort of project for them.

Industry/Entity Type

Business

Requirements
Must have
• Portfolio page needs to be updated to have LOTS more pictures and have them in an organized manner where it's easy to navigate through them. My other main thing is that I want to keep the same look and feel that it has with the nice woodgrain background, user friendly layout of links, etc.

```html
<!DOCTYPE html>
<html lang="en">
<head>
<meta charset="utf-8">
<title>Ferrow Builders – building and renovation company</title>
<link href="https://fonts.googleapis.com/css2?family=Comfortaa:wght@400;600&family=PT+Sans:wght@400&display=swap" rel="stylesheet">
<style>
:root{
  --wood-dark:#2e1d12;
  --wood-mid:#4a3020;
  --wood-light:#5b3c28;
  --panel:rgba(30,18,10,.35);
  --panel-edge:rgba(15,8,4,.6);
  --panel-hi:rgba(255,230,200,.08);
  --cream:#efe2cc;
  --text:#eadbc6;
  --parchment:#d9cfa4;
  --parchment-dark:#bfb283;
  --ink:#3a2a1a;
  --frame:#e6d9c8;
}
*{margin:0;padding:0;box-sizing:border-box}
html,body{width:1200px;height:1146px;overflow:hidden}
body{
  position:relative;
  font-family:"PT Sans",sans-serif;
  color:var(--text);
  background:
    repeating-linear-gradient(90deg,rgba(0,0,0,.08) 0 3px,transparent 3px 11px,rgba(255,220,180,.04) 11px 14px,transparent 14px 23px),
    repeating-linear-gradient(90deg,rgba(0,0,0,.1) 0 40px,rgba(255,220,180,.03) 40px 95px,rgba(0,0,0,.06) 95px 160px),
    radial-gradient(ellipse at 50% 40%,var(--wood-light),var(--wood-mid) 60%,var(--wood-dark));
}
.brand{position:absolute;left:120px;top:26px;font-family:"Comfortaa",sans-serif;color:var(--cream)}
.brand-name{font-size:45px;font-weight:600;letter-spacing:.5px}
.brand-tagline{position:absolute;left:149px;top:60px;white-space:nowrap;font-size:18px}
.panel{position:absolute;background:var(--panel);border:1px solid var(--panel-edge);border-radius:10px;
  box-shadow:inset 0 1px 0 var(--panel-hi),0 2px 6px rgba(0,0,0,.35)}
.panel-main{left:103px;top:128px;width:981px;height:409px}
.panel-strip{left:103px;top:556px;width:981px;height:146px}
.panel-services{left:104px;top:722px;width:311px;height:278px}
.panel-footer{left:103px;top:1035px;width:981px;height:92px}
.main-nav{position:absolute;left:128px;top:157px;width:187px}
.main-nav a{display:flex;align-items:center;justify-content:center;height:52px;margin-bottom:9px;
  background:linear-gradient(180deg,var(--parchment),var(--parchment-dark));
  color:var(--ink);text-decoration:none;font-family:"Comfortaa",sans-serif;font-size:19px;font-weight:600;
  box-shadow:2px 3px 5px rgba(0,0,0,.5);border-radius:2px 6px 3px 5px}
.hero{position:absolute;left:365px;top:154px;width:699px;height:355px;border:1px solid #6a4a33;
  background:linear-gradient(135deg,#b07a45,#7a4a26 45%,#c08a50 70%,#5a3520)}
.thumbs{position:absolute;left:155px;top:580px;display:flex;gap:22px}
.thumb{width:127px;height:100px;border:3px solid var(--frame);box-shadow:0 2px 4px rgba(0,0,0,.5)}
.t1{background:linear-gradient(135deg,#8a6a4a,#c9b08a)}
.t2{background:linear-gradient(135deg,#7a8fa0,#d8d0c8)}
.t3{background:linear-gradient(135deg,#b89a60,#4a3020)}
.t4{background:linear-gradient(135deg,#8a5a3a,#d8c8a8)}
.t5{background:linear-gradient(135deg,#c0a080,#e8e0d8)}
.t6{background:linear-gradient(135deg,#a0522d,#5a2e1a)}
.arrow{position:absolute;top:606px}
.arrow-prev{left:111px}.arrow-next{left:1047px}
.section-title{font-family:"Comfortaa",sans-serif;font-size:23px;color:var(--cream);font-weight:600}
.services-title{position:absolute;left:126px;top:734px}
.service-list{position:absolute;left:126px;top:780px;list-style:none}
.service-list li{display:flex;align-items:center;height:29.2px;font-size:14.5px}
.service-list svg{margin-right:10px}
.more{position:absolute;font-size:14px;color:var(--text);text-decoration:none}
.more-services{left:309px;top:973px}
.more-welcome{left:958px;top:994px}
.welcome-title{position:absolute;left:438px;top:726px;font-weight:400}
.welcome-text{position:absolute;left:438px;top:774px;width:335px;font-size:13px;line-height:20.9px;text-align:justify}
.welcome-text p+p{margin-top:20.9px}
.photo{position:absolute;border:3px solid var(--frame);box-shadow:3px 4px 8px rgba(0,0,0,.6)}
.photo-back{left:905px;top:780px;width:170px;height:165px;transform:rotate(11deg);
  background:linear-gradient(160deg,#1c2450,#6a3a20 60%,#c07a30)}
.photo-front{left:795px;top:805px;width:178px;height:155px;background:linear-gradient(135deg,#e8e4dc,#b0a898 60%,#7a6a58)}
.footer-nav{position:absolute;left:103px;top:1054px;width:981px;text-align:center;font-size:14.5px}
.footer-nav a{color:var(--text);text-decoration:none;margin:0 12px}
.copyright{position:absolute;left:103px;top:1087px;width:981px;text-align:center;font-size:14px}
</style>
</head>
<body>
<header class="brand">
  <div class="brand-name">Ferrow Builders</div>
  <div class="brand-tagline">building and rennovation company</div>
</header>

<div class="panel panel-main"></div>
<nav class="main-nav">
  <a href="#">Home</a><a href="#">About Us</a><a href="#">Services</a>
  <a href="#">Portfolio</a><a href="#">Process</a><a href="#">Contact</a>
</nav>
<div class="hero" role="img" aria-label="Photo of a renovated kitchen and dining room with wood cabinets and chandelier"></div>

<div class="panel panel-strip"></div>
<svg class="arrow arrow-prev" width="26" height="32" viewBox="0 0 26 32"><path d="M20 3 L6 16 L20 29" fill="none" stroke="#efe2cc" stroke-width="6"/></svg>
<div class="thumbs">
  <div class="thumb t1" role="img" aria-label="Living room with fireplace"></div>
  <div class="thumb t2" role="img" aria-label="Bedroom with blue walls"></div>
  <div class="thumb t3" role="img" aria-label="Den with ceiling fan"></div>
  <div class="thumb t4" role="img" aria-label="Dining room with curtains"></div>
  <div class="thumb t5" role="img" aria-label="Guest bedroom"></div>
  <div class="thumb t6" role="img" aria-label="Dining room with chandelier"></div>
</div>
<svg class="arrow arrow-next" width="26" height="32" viewBox="0 0 26 32"><path d="M6 3 L20 16 L6 29" fill="none" stroke="#efe2cc" stroke-width="6"/></svg>

<div class="panel panel-services"></div>
<h2 class="section-title services-title">Services</h2>
<ul class="service-list">
  <li><svg width="14" height="13" viewBox="0 0 14 13"><rect x="1" y="3" width="9" height="9" fill="none" stroke="#eadbc6" stroke-width="1.5"/><path d="M3 7 L6 10 L13 1" fill="none" stroke="#eadbc6" stroke-width="2"/></svg>Bathrooms</li>
  <li><svg width="14" height="13" viewBox="0 0 14 13"><rect x="1" y="3" width="9" height="9" fill="none" stroke="#eadbc6" stroke-width="1.5"/><path d="M3 7 L6 10 L13 1" fill="none" stroke="#eadbc6" stroke-width="2"/></svg>Custom Cabinetry</li>
  <li><svg width="14" height="13" viewBox="0 0 14 13"><rect x="1" y="3" width="9" height="9" fill="none" stroke="#eadbc6" stroke-width="1.5"/><path d="M3 7 L6 10 L13 1" fill="none" stroke="#eadbc6" stroke-width="2"/></svg>Frame and Finish Carpentry</li>
  <li><svg width="14" height="13" viewBox="0 0 14 13"><rect x="1" y="3" width="9" height="9" fill="none" stroke="#eadbc6" stroke-width="1.5"/><path d="M3 7 L6 10 L13 1" fill="none" stroke="#eadbc6" stroke-width="2"/></svg>Outdoor Living and Decks</li>
  <li><svg width="14" height="13" viewBox="0 0 14 13"><rect x="1" y="3" width="9" height="9" fill="none" stroke="#eadbc6" stroke-width="1.5"/><path d="M3 7 L6 10 L13 1" fill="none" stroke="#eadbc6" stroke-width="2"/></svg>Energy Efficient/Green Remodeling</li>
  <li><svg width="14" height="13" viewBox="0 0 14 13"><rect x="1" y="3" width="9" height="9" fill="none" stroke="#eadbc6" stroke-width="1.5"/><path d="M3 7 L6 10 L13 1" fill="none" stroke="#eadbc6" stroke-width="2"/></svg>Doors and Windows</li>
  <li><svg width="14" height="13" viewBox="0 0 14 13"><rect x="1" y="3" width="9" height="9" fill="none" stroke="#eadbc6" stroke-width="1.5"/><path d="M3 7 L6 10 L13 1" fill="none" stroke="#eadbc6" stroke-width="2"/></svg>Custom Concrete</li>
</ul>
<a class="more more-services" href="#">View more [+]</a>

<h2 class="section-title welcome-title">Welcome to Ferrow Builders</h2>
<div class="welcome-text">
  <p>Welcome to Ferrow Builders, a locally owned and operated residential and commercial construction company serving the greater New Orleans area and southeastern Louisiana. We are experts in all forms of residential building, remodeling and renovations.</p>
  <p>Apart from general contracting, our specialty is custom millwork installations which has become our most sought after service, and has brought us into the commercial market and now accounts for a vast majority of our sales.</p>
</div>
<div class="photo photo-back" role="img" aria-label="Backyard patio at night with string lights"></div>
<div class="photo photo-front" role="img" aria-label="Bright living room with white fireplace"></div>
<a class="more more-welcome" href="#">View more [+]</a>

<footer>
  <div class="panel panel-footer"></div>
  <nav class="footer-nav">
    <a href="#">Home</a>|<a href="#">About Us</a>|<a href="#">Services</a>|<a href="#">Portfolio</a>|<a href="#">Process</a>|<a href="#">Contact</a>
  </nav>
  <p class="copyright">Copyright © 2012 FerrowBuilders.example . All Rights Reserved.</p>
</footer>
</body>
</html>
```